EB-5 Regional Center needs a Web design

Marlowfield Equity Partners is an expanding EB-r regional center. We have been successful in sponsoring multiple projects of third-party developers and placing EB-5, B-1, and Private Investments into multiple projects.

We are now partnering directly with project developers in the energy and healthcare to raise foreign capital for projects in those industries. The foreign capital is used as project equity and our collective balance sheets are used to guarantee debt to complete the funding of the projects.

We need a web site where we can post our company credentials, the bios of each partner, a document page for each of our projects where we can post specific project related documents which foreign investors can read, and we will need a section where foreign investors can fill out investor forms confirming that they are qualified investors and leaving their contact so that our agents and executives can make contact.

The final design should reflect the exceptional experience of the partners and our financial strength and stability.

We do have a logo we would want to use on the web design.

Target Market(s)

EB-5 Investors, B-1 Investors, Private Equity and other investors seeking quality investment in job creating US projects.

Coding

Coded - Design and coding required

Number of Pages Required

5+ page

Font styles to use
Sans Serif

Requirements
Must have
• Pages to display company info, partner bios, projects completed, and a projects in-process page where we can post documents and info on projects for which we are seeking foreign investment. We also need a section where investors can enter their qualifying personal information and leave contact information for us.

```html
<!DOCTYPE html>
<html lang="en">
<head>
<meta charset="utf-8">
<title>Marlowfield Equity Partners</title>
<link rel="stylesheet" href="https://fonts.googleapis.com/css2?family=Open+Sans:wght@400;600;700;800&display=swap">
<style>
:root{
  --ink:#2b2b2b;
  --text:#555;
  --muted:#8a8a8a;
  --line:#d6d6d6;
  --white:#fff;
  --soft:#f1f1f1;
  --band:#ececec;
  --dark:#6b6b6b;
  --btn:#555;
  --accent:#3a3a3a;
}
*{box-sizing:border-box;margin:0;padding:0}
html,body{width:1200px;height:4184px;overflow:hidden}
body{font-family:"Open Sans",sans-serif;color:var(--text);background:var(--white);font-size:15px;line-height:1.55}
.btn{display:inline-block;background:var(--btn);color:var(--white);font-size:13px;font-weight:700;letter-spacing:1px;text-transform:uppercase;padding:8px 20px}
.section-title{text-align:center;font-size:30px;font-weight:800;color:var(--ink);letter-spacing:1px}
.section-title::after{content:"";display:block;width:48px;height:3px;background:var(--ink);margin:14px auto 0}

/* header */
.site-header{height:112px;position:relative}
.brand{position:absolute;left:120px;top:24px;display:flex;align-items:center;gap:14px}
.brand-mark{width:40px;height:40px;background:var(--accent)}
.brand-name{font-size:26px;font-weight:700;color:var(--accent);line-height:1.1}
.main-nav{position:absolute;left:540px;top:68px;display:flex;gap:6px}
.main-nav a{font-size:15px;font-weight:600;color:var(--ink);padding:5px 12px;text-transform:uppercase;text-decoration:none}
.main-nav a.active{background:var(--btn);color:var(--white)}
.header-mail{position:absolute;left:880px;top:16px;display:flex;gap:12px;align-items:center;font-size:14px;color:var(--ink)}
.header-mail small{display:block;font-size:12px;color:var(--muted)}

/* hero */
.hero{height:608px;position:relative;background:linear-gradient(120deg,#3c4b63 0%,#8a97a8 35%,#c9ccd2 50%,#8c6f6a 70%,#3a3d49 100%)}
.hero-copy{position:absolute;left:0;right:0;top:48px;text-align:center;color:var(--white)}
.hero-copy h1{font-size:52px;font-weight:800;line-height:1.1;letter-spacing:2px}
.hero-copy h1 span{display:block;font-size:40px}
.hero-copy .btn{margin-top:18px;background:#4a4a4a}

/* welcome */
.welcome{height:520px;position:relative}
.welcome-brand{position:absolute;left:150px;top:110px;width:330px;height:300px;display:flex;flex-direction:column;align-items:center;justify-content:center;gap:22px}
.welcome-brand .square{width:120px;height:120px;background:#8c8c8c}
.welcome-brand p{font-size:28px;font-weight:700;color:#8c8c8c;text-align:center;line-height:1.2}
.welcome-divider{position:absolute;left:580px;top:110px;width:2px;height:300px;background:var(--line)}
.welcome-copy{position:absolute;left:660px;top:80px;width:440px}
.welcome-copy h3{font-size:18px;font-weight:700;color:var(--ink);letter-spacing:1px}
.welcome-copy h2{font-size:32px;font-weight:800;color:var(--ink);line-height:1.15;margin-top:4px}
.welcome-copy h2::after{content:"";display:block;width:48px;height:3px;background:var(--ink);margin-top:14px}
.welcome-copy p{margin-top:18px;font-size:16px}
.welcome-copy .btn{margin-top:26px}

/* services */
.services{height:480px;background:var(--band);padding-top:48px}
.service-grid{display:flex;gap:16px;margin:56px 0 0 128px}
.service-card{width:224px;height:268px;background:var(--white);text-align:center;padding:46px 18px 0}
.service-card svg{width:56px;height:56px}
.service-card h4{font-size:14px;font-weight:800;color:var(--ink);margin:22px 0 8px;text-transform:uppercase}
.service-card p{font-size:12px;line-height:1.45}

/* team */
.team{height:660px;position:relative;padding-top:64px}
.team-row{position:absolute;top:180px;left:0;right:0}
.member{position:absolute;width:320px;text-align:center}
.member .portrait{width:300px;height:300px;margin:0 auto;clip-path:polygon(50% 0,100% 50%,50% 100%,0 50%)}
.member h4{font-size:16px;font-weight:800;color:var(--ink);margin-top:12px;text-transform:uppercase}
.member p{font-size:12px;line-height:1.45;padding:0 50px;margin-top:4px}
.member .btn{font-size:10px;padding:4px 14px;margin-top:10px}
.arrow{position:absolute;top:340px;width:32px;height:32px;border-radius:50%;background:var(--band);display:flex;align-items:center;justify-content:center}

/* projects */
.projects{height:720px;background:linear-gradient(180deg,#e6e6e6,#f4f4f4);position:relative;padding-top:64px}
.project-grid{position:absolute;left:128px;top:148px;width:944px;height:500px}
.project{position:absolute}
.project .shot{width:100%}
.project h5{font-size:13px;font-weight:800;color:var(--ink);margin-top:10px;text-transform:uppercase}
.project p{font-size:11px;line-height:1.4}
.projects .btn{position:absolute;left:0;right:0;margin:0 auto;width:190px;text-align:center;top:608px}

/* contact */
.contact{height:688px;background:var(--dark);position:relative;padding-top:160px}
.contact .section-title{color:var(--white)}
.contact .section-title::after{background:var(--white)}
.contact-form{position:absolute;left:260px;top:252px;width:680px;height:368px;background:var(--white);padding:44px 60px}
.field-row{display:flex;gap:20px;margin-bottom:16px}
.field{flex:1;height:42px;border:1px solid var(--line);font-size:11px;color:var(--muted);padding:12px 14px;text-transform:uppercase}
.field.message{height:104px}
.contact-form .btn{display:block;width:110px;margin:20px auto 0;text-align:center}

/* footer */
.site-footer{height:396px;background:var(--soft);position:relative}
.footer-brand{position:absolute;left:130px;top:70px;display:flex;flex-direction:column;gap:16px;align-items:center;width:300px}
.footer-brand .square{width:90px;height:90px;background:#8c8c8c}
.footer-brand p{font-size:22px;font-weight:700;color:#8c8c8c;text-align:center;line-height:1.2}
.footer-col{position:absolute;top:50px}
.footer-col h6{font-size:15px;font-weight:800;color:var(--ink);text-transform:uppercase}
.footer-col h6::after{content:"";display:block;width:30px;height:2px;background:var(--ink);margin:8px 0 14px}
.footer-col li{list-style:none;font-size:13px;line-height:1.7;text-transform:uppercase;color:var(--text)}
.info{display:flex;gap:12px;align-items:center;margin-bottom:16px;font-size:12px;line-height:1.4}
.dot{width:26px;height:26px;border-radius:50%;background:#6a6a6a;flex:none;display:flex;align-items:center;justify-content:center}
.copyright{position:absolute;right:120px;bottom:44px;font-size:10px;color:var(--muted)}
</style>
</head>
<body>

<header class="site-header">
  <div class="brand"><span class="brand-mark"></span><span class="brand-name">Marlowfield<br>Equity Partners</span></div>
  <nav class="main-nav">
    <a class="active">Home</a><a>About us</a><a>Services</a><a>Team</a><a>Projects</a><a>Contact us</a>
  </nav>
  <div class="header-mail">
    <span class="dot"><svg width="14" height="10" viewBox="0 0 14 10"><rect x=".5" y=".5" width="13" height="9" fill="none" stroke="#fff"/><path d="M.5 .5 7 6 13.5 .5" fill="none" stroke="#fff"/></svg></span>
    <div><small>E-MAIL US</small>info@marlowfield.com</div>
  </div>
</header>

<section class="hero" role="img" aria-label="Photo of two business people shaking hands over a city skyline">
  <div class="hero-copy">
    <h1>EQUITY<span>PARTNERS</span></h1>
    <span class="btn">Read more</span>
  </div>
</section>

<section class="welcome">
  <div class="welcome-brand"><span class="square"></span><p>Marlowfield<br>Equity Partners</p></div>
  <div class="welcome-divider"></div>
  <div class="welcome-copy">
    <h3>WELCOME TO</h3>
    <h2>MARLOWFIELD EQUITY PARTNERS.</h2>
    <p>Lorem ipsum dolor sit amet, consectetur adipiscing elit, sed do eiusmod tempor incididunt ut labore et dolore magna aliqua. Ut enim ad minim veniam, quis nostrud exercitation ullamco laboris nisi ut aliquip ex ea commodo consequat. Duis aute irure dolor in reprehenderit in voluptate velit esse cillum dolore eu fugiat nulla pariatur. Excepteur sint occaecat cupidatat non proident, sunt in culpa.</p>
    <span class="btn">Read more</span>
  </div>
</section>

<section class="services">
  <h2 class="section-title">OUR SERVICES</h2>
  <div class="service-grid">
    <div class="service-card">
      <svg viewBox="0 0 56 56"><path d="M8 6v42h42" fill="none" stroke="#444" stroke-width="2"/><rect x="16" y="32" width="6" height="14" fill="#444"/><rect x="27" y="24" width="6" height="22" fill="#444"/><rect x="38" y="16" width="6" height="30" fill="#444"/><path d="M14 26 26 16 34 20 46 8" fill="none" stroke="#444" stroke-width="2"/></svg>
      <h4>Private Equity</h4>
      <p>Lorem ipsum dolor sit amet, consectetur adipiscing elit, sed do eiusmod tempor incididunt ut labore et dolore magna aliqua.</p>
    </div>
    <div class="service-card">
      <svg viewBox="0 0 56 56"><rect x="14" y="10" width="34" height="20" fill="none" stroke="#444" stroke-width="2"/><rect x="8" y="18" width="34" height="20" fill="#fff" stroke="#444" stroke-width="2"/><circle cx="25" cy="28" r="5" fill="none" stroke="#444" stroke-width="2"/><path d="M10 44h30M14 48h22" stroke="#444" stroke-width="2"/></svg>
      <h4>Private Debt</h4>
      <p>Lorem ipsum dolor sit amet, consectetur adipiscing elit, sed do eiusmod tempor incididunt ut labore et dolore magna aliqua.</p>
    </div>
    <div class="service-card">
      <svg viewBox="0 0 56 56"><path d="M46 20A20 20 0 0 0 10 18M10 36a20 20 0 0 0 36 2" fill="none" stroke="#444" stroke-width="2"/><path d="M10 10v8h8M46 46v-8h-8" fill="none" stroke="#444" stroke-width="2"/><text x="28" y="35" text-anchor="middle" font-family="Open Sans,sans-serif" font-weight="700" font-size="20" fill="#444">$</text></svg>
      <h4>Alternative Funds</h4>
      <p>Lorem ipsum dolor sit amet, consectetur adipiscing elit, sed do eiusmod tempor incididunt ut labore et dolore magna aliqua.</p>
    </div>
    <div class="service-card">
      <svg viewBox="0 0 56 56"><rect x="14" y="8" width="28" height="40" fill="none" stroke="#444" stroke-width="2"/><path d="M20 14h4M32 14h4M20 22h4M32 22h4M20 30h4M32 30h4M8 48h40" stroke="#444" stroke-width="2"/><rect x="24" y="38" width="8" height="10" fill="#444"/></svg>
      <h4>Commercial Property</h4>
      <p>Lorem ipsum dolor sit amet, consectetur adipiscing elit, sed do eiusmod tempor incididunt ut labore et dolore magna aliqua.</p>
    </div>
  </div>
</section>

<section class="team">
  <h2 class="section-title">OUR TEAM</h2>
  <span class="arrow" style="left:66px"><svg width="10" height="12" viewBox="0 0 10 12"><path d="M8 1 2 6l6 5" fill="none" stroke="#555" stroke-width="2"/></svg></span>
  <span class="arrow" style="left:1106px"><svg width="10" height="12" viewBox="0 0 10 12"><path d="M2 1l6 5-6 5" fill="none" stroke="#555" stroke-width="2"/></svg></span>
  <div class="team-row">
    <div class="member" style="left:140px">
      <div class="portrait" role="img" aria-label="Portrait photo of partner Daniel" style="background:linear-gradient(160deg,#9aa4a8,#3e4448)"></div>
      <h4>Daniel</h4>
      <p>Lorem ipsum dolor sit amet, consectetur adipiscing elit, sed do eiusmod tempor incididunt ut labore et dolore.</p>
      <span class="btn">View bio</span>
    </div>
    <div class="member" style="left:440px">
      <div class="portrait" role="img" aria-label="Portrait photo of partner Marco" style="background:linear-gradient(160deg,#5a5a5a,#1e1e22)"></div>
      <h4>Marco</h4>
      <p>Lorem ipsum dolor sit amet, consectetur adipiscing elit, sed do eiusmod tempor incididunt ut labore et dolore.</p>
      <span class="btn">View bio</span>
    </div>
    <div class="member" style="left:740px">
      <div class="portrait" role="img" aria-label="Portrait photo of partner Owen Tate" style="background:linear-gradient(160deg,#c9d3da,#6e7e88)"></div>
      <h4>Owen Tate</h4>
      <p>Lorem ipsum dolor sit amet, consectetur adipiscing elit, sed do eiusmod tempor incididunt ut labore et dolore.</p>
      <span class="btn">View bio</span>
    </div>
  </div>
</section>

<section class="projects">
  <h2 class="section-title">PROJECTS</h2>
  <div class="project-grid">
    <div class="project" style="left:0;top:0;width:464px">
      <div class="shot" role="img" aria-label="Photo of a hand over a glowing green market chart" style="height:372px;background:linear-gradient(180deg,#1b1f1c,#24402c 70%,#1a1d1b)"></div>
      <h5>Sed ut perspiciatis unde omnis iste natus error</h5>
      <p>Lorem ipsum dolor sit amet, consectetur adipiscing elit, sed do eiusmod tempor incididunt ut labore et dolore magna aliqua ut enim.</p>
    </div>
    <div class="project" style="left:480px;top:0;width:224px">
      <div class="shot" role="img" aria-label="Photo of hands working on a laptop with charts" style="height:192px;background:linear-gradient(135deg,#7c8a96,#2f3a44)"></div>
      <h5>Lorem ipsum dolor sit</h5>
      <p>Lorem ipsum dolor sit amet, consectetur adipiscing elit.</p>
    </div>
    <div class="project" style="left:720px;top:0;width:224px">
      <div class="shot" role="img" aria-label="Photo of a financial district at dusk with rising bars" style="height:192px;background:linear-gradient(135deg,#3b2d4a,#b06a6a)"></div>
      <h5>Lorem ipsum dolor sit</h5>
      <p>Lorem ipsum dolor sit amet, consectetur adipiscing elit.</p>
    </div>
    <div class="project" style="left:480px;top:272px;width:224px">
      <div class="shot" role="img" aria-label="Photo of a business presentation with a rising chart" style="height:100px;background:linear-gradient(135deg,#2f4f6e,#a6b9c8)"></div>
      <h5>Lorem ipsum dolor sit</h5>
      <p>Lorem ipsum dolor sit amet, consectetur adipiscing elit.</p>
    </div>
    <div class="project" style="left:720px;top:272px;width:224px">
      <div class="shot" role="img" aria-label="Photo of stacked coins with growing plants" style="height:100px;background:linear-gradient(135deg,#5a6b2e,#d2b25a)"></div>
      <h5>Lorem ipsum dolor sit</h5>
      <p>Lorem ipsum dolor sit amet, consectetur adipiscing elit.</p>
    </div>
  </div>
  <span class="btn">View all projects</span>
</section>

<section class="contact">
  <h2 class="section-title">CONTACT US</h2>
  <div class="contact-form">
    <div class="field-row"><span class="field">Name</span><span class="field">E-mail</span></div>
    <div class="field-row"><span class="field">Phone</span><span class="field">Subject</span></div>
    <div class="field message">Message</div>
    <span class="btn">Submit</span>
  </div>
</section>

<footer class="site-footer">
  <div class="footer-brand"><span class="square"></span><p>Marlowfield<br>Equity Partners</p></div>
  <div class="footer-col" style="left:488px">
    <h6>Menu</h6>
    <ul><li>Home</li><li>About us</li><li>Services</li><li>Team</li><li>Projects</li><li>Contact us</li></ul>
  </div>
  <div class="footer-col" style="left:652px">
    <h6>Contact us</h6>
    <div class="info"><span class="dot"><svg width="10" height="14" viewBox="0 0 10 14"><path d="M5 13S1 8 1 5a4 4 0 0 1 8 0c0 3-4 8-4 8z" fill="#fff"/></svg></span><span>2200 Harbor Lane<br>Tustin, CA 92780</span></div>
    <div class="info"><span class="dot"><svg width="12" height="12" viewBox="0 0 12 12"><path d="M2 1h3l1 3-2 1a7 7 0 0 0 3 3l1-2 3 1v3c-6 0-9-3-9-9z" fill="#fff"/></svg></span><span>Call Us<br>800-000-0000</span></div>
    <div class="info"><span class="dot"><svg width="12" height="9" viewBox="0 0 12 9"><rect x=".5" y=".5" width="11" height="8" fill="none" stroke="#fff"/><path d="M.5 .5 6 5l5.5-4.5" fill="none" stroke="#fff"/></svg></span><span>E-Mail Us<br>info@marlowfield.com</span></div>
  </div>
  <div class="footer-col" style="left:940px">
    <h6>Follow us</h6>
    <div class="info"><span class="dot"></span><span>Like us on<br>FRIENDLOOP</span></div>
    <div class="info"><span class="dot"></span><span>Follow us on<br>CHIRPLINE</span></div>
    <div class="info"><span class="dot"></span><span>Follow us on<br>WORKGRAPH</span></div>
  </div>
  <p class="copyright">Copyright © 2024 All Rights Reserved</p>
</footer>

</body>
</html>
```